PPT template for boutique strategic planning, accounting and taxation firm

We are a boutique firm that provides strategic, accounting and tax advice to our clients. The work we are doing is increasingly strategic work and we are required to produce reports and presentations and our current templates are simply not sufficient.
As you can see from the examples attached, we have very limited skills in house re design! We have attached a PPT document and word document (that should be PPT) that we use regularly as examples of the content. Excel worksheets are regularly embedded into the presentation (in both blue and orange - see below re colours)
Not specific to one area but typically these clients are famous for their own brand and are creating value in their industry through creating their own brand and we want to produce documents of a similar standard.
A Powerpoint Document Slide Template
Cover page layout, back page, intermediate page heading, in colours and styles based on the logo, title styles, and an intermediate or chapter heading slide style. Many of our presentations contain slides with tables, diagrams, flowcharts and text, including simple lists of bullet points. As above, you will see in our style guide that we have three coloured logos – we would like one version in blue and one version in orange please. Again, the cover should be bold and draw attention but remain professional.
We are looking for something that works in both 4:3 and 16:9 (or two templates please)
We like a clear professional and simple look.
Deliverable: PowerPoint template file (.potx extension) for PowerPoint 2007 with at least a “cover” layout, a “title and content” layout, and a simplified slide layout, as well as “back cover”. Please embed any fonts used.
Target Market(s)
Many of our clients are retail clients or have strong brands of their own.
Industry/Entity Type
Accounting
Requirements
Must have
- Harrowby & Co logo on each page.
Must have a cover page (please be bold but professional)
A selection of "standard" slides - dot points, detailed written content, example diagrams, flow charts etc.
A back cover
Nice to have
- We would like to have a copy done in both the blue and orange versions attached. Happy for the winner to complete the other colour after the winner is selected.
Prefer Arial logo but open to suggestions. Must be easy to read and professional
Should not have
- Nothing cartoonish

```html
<!DOCTYPE html>
<html lang="en">
<head>
<meta charset="utf-8">
<title>Harrowby &amp; Co — Presentation Template</title>
<link rel="stylesheet" href="https://fonts.googleapis.com/css2?family=Jost:wght@300;400;500;600;700&display=swap">
<style>
:root{
  --orange:#f47c20;
  --charcoal:#474b52;
  --charcoal-dark:#3f434a;
  --board:#7d8189;
  --paper:#ffffff;
  --paper-soft:#f6f6f6;
  --rule:#e2e2e2;
  --placeholder:#e9e9e9;
  --muted:#8b8f96;
  --ink:#3a3d42;
  --blue:#4fb0e3;
  --green:#a6d13b;
  --pink:#e25475;
  --purple:#a43fae;
  --grey-series:#9ea5ad;
}
*{margin:0;padding:0;box-sizing:border-box}
html,body{width:1064px;height:1200px;overflow:hidden;background:var(--board)}
body{font-family:"Jost",Arial,sans-serif;color:var(--ink)}
.board{position:absolute;left:0;top:0;width:1200px;height:1353px;transform:scale(0.886667);transform-origin:0 0;background:var(--board)}
.slide{position:absolute;width:582px;height:435px;overflow:hidden;background:var(--paper)}
.abs{position:absolute}

/* brand name lockup */
.brand{display:flex;align-items:center;gap:10px}
.brand-dot{border-radius:50%;background:var(--orange);flex:none}
.brand-name{font-weight:600;letter-spacing:-0.5px;line-height:1;white-space:nowrap}
.lockup{display:flex;flex-direction:column;gap:7px}
.tagline{font-size:12.5px;font-weight:500;white-space:nowrap;line-height:1.2}

/* cover */
.cover .brand{left:104px;top:148px}
.cover .brand-dot,.back .brand-dot{width:84px;height:84px}
.cover .brand-name{font-size:44px;color:var(--charcoal);letter-spacing:-1px}
.cover .tagline{color:var(--charcoal)}
.cover .title{right:21px;top:288px;font-size:29px;font-weight:600;color:var(--charcoal);text-align:right;line-height:1}
.cover .date{right:21px;top:323px;font-size:14px;color:var(--orange)}
.cover .band{left:0;top:365px;width:582px;height:70px;background:var(--charcoal);border-bottom:3px solid var(--orange)}
.cover .band-title{left:11px;top:14px;font-size:22px;color:#fff;font-weight:300;letter-spacing:-0.3px}
.cover .band-title b{font-weight:700}
.cover .band-sub{left:11px;top:39px;font-size:13px;color:var(--orange)}
.cover .band-sub b{font-weight:600}
.client-mark{left:502px;top:8px;width:68px;height:50px;background:var(--charcoal-dark);border:1px solid #5a5e65}

/* chapter */
.chapter{background:var(--orange);color:#fff;text-align:center}
.chapter .heading{left:0;width:582px;top:186px;font-size:44px;font-weight:600;letter-spacing:-0.5px}
.chapter .subline{left:92px;width:398px;top:240px;display:flex;align-items:center;gap:10px;font-size:14px}
.chapter .subline::before,.chapter .subline::after{content:"";flex:1;height:1px;background:#fff;opacity:.8}
.chapter .page{left:0;width:582px;top:283px;font-size:10px}

/* standard slide */
.header-title{left:0;width:582px;text-align:center;top:0;font-size:31px;font-weight:300;color:var(--orange);letter-spacing:-0.3px}
.header-sub{left:0;width:582px;text-align:center;top:35px;font-size:10.5px;color:var(--charcoal);letter-spacing:-0.1px}
.header-sub b{font-weight:600}
.body-area{left:0;top:54px;width:582px;height:346px;background:var(--paper-soft)}
.footer{left:0;top:400px;width:582px;height:35px;background:var(--charcoal);display:flex;align-items:center;padding:0 10px;color:#fff}
.footer .brand{gap:6px}
.footer .brand-dot{width:22px;height:22px}
.footer .brand-name{font-size:18px;color:#fff}
.footer .divider{width:2px;height:12px;background:#fff;margin:0 12px}
.footer .deck{font-size:10.5px;font-weight:600;letter-spacing:-0.2px}
.footer .deck span{color:var(--orange)}
.footer .deck em{font-style:normal;font-weight:400}
.footer .page{margin-left:auto;color:var(--orange);font-size:10px}

/* content slide */
.content-title{left:72px;top:77px;font-size:17px;color:var(--orange);font-weight:600}
.content-title span{font-weight:400}
.step-no{width:40px;height:40px;border-radius:50%;background:var(--orange);color:#fff;font-size:30px;font-weight:600;display:flex;align-items:center;justify-content:center}
.step-text{width:212px;font-size:10px;line-height:12.5px;text-align:justify;letter-spacing:.6px}
.step-text b{font-weight:600}
.sub-list{list-style:none;font-size:10.5px}
.sub-list li{display:flex;align-items:center;gap:6px;height:26px}
.sub-list li::before{content:"";width:9px;height:9px;border-radius:50%;border:2px solid var(--orange)}
.portrait-slot{left:301px;top:72px;width:247px;height:310px;background:var(--placeholder);border:1px solid #dcdcdc}

/* tables */
.table-label{display:flex;align-items:center;gap:6px;font-size:17px;color:var(--charcoal)}
.table-label b{font-weight:600}
.data-table{border-collapse:collapse;width:260px;font-size:6.5px;table-layout:fixed}
.data-table th{height:24px;font-size:10px;font-weight:500;color:#fff;text-align:center}
.data-table td{height:25.3px;padding:0 3px;border-bottom:1px solid var(--rule);color:#777;vertical-align:middle}
.data-table td.no{color:var(--orange);font-weight:600;font-size:10px;text-align:center}
.data-table td.c{text-align:center}
.data-table .foot td{height:26px;font-size:10px;color:#fff;text-align:center;border:none}
.light th{background:var(--charcoal)}
.light td{background:#fff}
.light .foot td{background:var(--orange)}
.dark th{background:var(--orange)}
.dark td{background:var(--charcoal);color:#cfd1d4;border-bottom:1px solid #55595f}
.dark .foot td{background:var(--muted)}

/* graphs */
.graph-label{font-size:17px;color:var(--charcoal)}
.graph-label b{font-weight:600}
.note-list{list-style:none;width:240px;font-size:8.5px;line-height:10px}
.note-list li{position:relative;padding-left:14px;margin-bottom:10px}
.note-list li::before{content:"";position:absolute;left:1px;top:1px;width:3px;height:6px;border:solid var(--orange);border-width:0 1.5px 1.5px 0;transform:rotate(40deg)}
.note-list b{font-weight:600}
.legend{list-style:none;font-size:8px}
.legend li{display:flex;align-items:center;gap:5px;height:10.5px}
.legend i{width:7px;height:7px;border-radius:50%}

/* back cover */
.back{background:var(--charcoal);color:#fff}
.back .brand{left:104px;top:150px}
.back .brand-name{font-size:44px;color:#fff;letter-spacing:-1px}
.back .tagline{color:#fff}
.contact{left:15px;font-size:8px;line-height:10px}
.contact h4{font-size:11px;color:var(--orange);font-weight:700;line-height:13px}
.web{right:68px;top:408px;font-size:10px;color:var(--orange)}
</style>
</head>
<body>
<div class="board">

  <!-- Cover -->
  <section class="slide cover" style="left:14px;top:10px">
    <div class="abs brand">
      <span class="brand-dot"></span>
      <div class="lockup">
        <span class="brand-name">Harrowby &amp; Co.</span>
        <p class="tagline">Accounting, Taxation &amp; Strategic Business Advisors</p>
      </div>
    </div>
    <h1 class="abs title">Presentation Title</h1>
    <p class="abs date">JAN 2014</p>
    <div class="abs band">
      <p class="abs band-title"><b>COMPANY</b> PRESENTATION</p>
      <p class="abs band-sub">to <b>Business</b>/Client</p>
      <div class="abs client-mark" role="img" aria-label="Client logo placeholder"></div>
    </div>
  </section>

  <!-- Chapter heading -->
  <section class="slide chapter" style="left:605px;top:10px">
    <h2 class="abs heading">New Chapter Heading</h2>
    <p class="abs subline">New Chapter Heading Subtitle</p>
    <p class="abs page">4</p>
  </section>

  <!-- Content with portrait image -->
  <section class="slide" style="left:14px;top:459px">
    <h2 class="abs header-title">IMAGE IN PORTRAIT VIEW</h2>
    <p class="abs header-sub">WITH AN EXAMPLE OF DIFFERENT TYPOGRAPHY</p>
    <div class="abs body-area"></div>
    <h3 class="abs content-title">Content <span>title</span></h3>
    <div class="abs step-no" style="left:26px;top:104px">1</div>
    <p class="abs step-text" style="left:73px;top:106px"><b>Aenean</b> ridiculus tortor quis interdum id habitant ad, natoque consectetuer nisl auctor libero quisque euismod ante inceptos malesuada ligula mattis.</p>
    <ul class="abs sub-list" style="left:93px;top:163px"><li>Pellentesque</li><li>Parturient</li><li>Ridiculus</li></ul>
    <div class="abs step-no" style="left:26px;top:254px">2</div>
    <p class="abs step-text" style="left:73px;top:248px"><b>Aenean</b> ridiculus tortor quis interdum id habitant ad, natoque consectetuer nisl auctor libero quisque euismod ante inceptos malesuada ligula mattis.</p>
    <ul class="abs sub-list" style="left:93px;top:305px"><li>Malesuada</li><li>Consectetuer</li><li>Natoque</li></ul>
    <div class="abs portrait-slot" role="img" aria-label="Portrait photograph placeholder"></div>
    <footer class="abs footer">
      <div class="brand"><span class="brand-dot"></span><span class="brand-name">Harrowby &amp; Co.</span></div>
      <span class="divider"></span>
      <p class="deck">COMPANY PRESENTATION <span><em>to</em> Business<em>/client</em></span></p>
      <span class="page">5</span>
    </footer>
  </section>

  <!-- Tables -->
  <section class="slide" style="left:605px;top:459px">
    <h2 class="abs header-title">COLOR STYLE TABLES</h2>
    <p class="abs header-sub">CHOOSE FROM A <b>LIGHT</b> OR <b>DARK</b> THEME</p>
    <div class="abs body-area" style="background:#fff"></div>
    <p class="abs table-label" style="left:24px;top:72px">
      <svg width="18" height="14" viewBox="0 0 18 14"><rect x="1" y="1" width="16" height="12" fill="none" stroke="#f47c20" stroke-width="1.6"/><path d="M1 5H17M1 9H17M6 1V13M12 1V13" stroke="#f47c20" stroke-width="1.2"/></svg>
      <span><b>Light</b> Theme</span></p>
    <p class="abs table-label" style="left:301px;top:72px">
      <svg width="18" height="14" viewBox="0 0 18 14"><rect x="1" y="1" width="16" height="12" fill="none" stroke="#f47c20" stroke-width="1.6"/><path d="M1 5H17M1 9H17M6 1V13M12 1V13" stroke="#f47c20" stroke-width="1.2"/></svg>
      <span><b>Dark</b> Theme</span></p>

    <table class="abs data-table light" style="left:22px;top:102px">
      <colgroup><col style="width:34px"><col style="width:98px"><col style="width:68px"><col style="width:60px"></colgroup>
      <tr><th>Item</th><th>Step/Action</th><th>Responsible</th><th>Target Date</th></tr>
      <tr><td class="no">1</td><td>Business X, Y, Z high level needs</td><td>Business X, Y, Z</td><td class="c">5/24/2013</td></tr>
      <tr><td class="no">2</td><td>Understand current situation and safety mana</td><td>Business X, Y, Z</td><td class="c">5/31/2013</td></tr>
      <tr><td class="no">3</td><td>Submit Proposal</td><td>Business X, Y, Z</td><td class="c">6/3/2013</td></tr>
      <tr><td class="no">4</td><td>Review Proposal</td><td>Business X, Y, Z</td><td class="c">TBD</td></tr>
      <tr><td class="no">5</td><td>Prepare Final Proposal &amp; Statement of Work (SOW)</td><td>Business X, Y, Z</td><td class="c">TBD</td></tr>
      <tr><td class="no">6</td><td>Complete and sign SOW</td><td>Business X, Y, Z</td><td class="c">TBD</td></tr>
      <tr><td class="no">7</td><td>Schedule project start date</td><td>Business X, Y, Z</td><td class="c">TBD</td></tr>
      <tr><td class="no">8</td><td>Kick-off Project</td><td>Business X, Y, Z</td><td class="c">TBD</td></tr>
      <tr><td class="no">9</td><td>Complete Project</td><td>Business X, Y, Z</td><td class="c">TBD</td></tr>
      <tr class="foot"><td colspan="4">* Additional Information</td></tr>
    </table>

    <table class="abs data-table dark" style="left:302px;top:102px">
      <colgroup><col style="width:34px"><col style="width:98px"><col style="width:68px"><col style="width:60px"></colgroup>
      <tr><th>Item</th><th>Step/Action</th><th>Responsible</th><th>Target Date</th></tr>
      <tr><td class="no">1</td><td>Business X, Y, Z high level needs</td><td>Business X, Y, Z</td><td class="c">5/24/2013</td></tr>
      <tr><td class="no">2</td><td>Understand current situation and safety mana</td><td>Business X, Y, Z</td><td class="c">5/31/2013</td></tr>
      <tr><td class="no">3</td><td>Submit Proposal</td><td>Business X, Y, Z</td><td class="c">6/3/2013</td></tr>
      <tr><td class="no">4</td><td>Review Proposal</td><td>Business X, Y, Z</td><td class="c">TBD</td></tr>
      <tr><td class="no">5</td><td>Prepare Final Proposal &amp; Statement of Work (SOW)</td><td>Business X, Y, Z</td><td class="c">TBD</td></tr>
      <tr><td class="no">6</td><td>Complete and sign SOW</td><td>Business X, Y, Z</td><td class="c">TBD</td></tr>
      <tr><td class="no">7</td><td>Schedule project start date</td><td>Business X, Y, Z</td><td class="c">TBD</td></tr>
      <tr><td class="no">8</td><td>Kick-off Project</td><td>Business X, Y, Z</td><td class="c">TBD</td></tr>
      <tr><td class="no">9</td><td>Complete Project</td><td>Business X, Y, Z</td><td class="c">TBD</td></tr>
      <tr class="foot"><td colspan="4">* Additional Information</td></tr>
    </table>

    <footer class="abs footer">
      <div class="brand"><span class="brand-dot"></span><span class="brand-name">Harrowby &amp; Co.</span></div>
      <span class="divider"></span>
      <p class="deck">COMPANY PRESENTATION <span><em>to</em> Business<em>/client</em></span></p>
      <span class="page">6</span>
    </footer>
  </section>

  <!-- Graphs -->
  <section class="slide" style="left:14px;top:908px">
    <h2 class="abs header-title">COLOR STYLE GRAPHS</h2>
    <p class="abs header-sub">CHOOSE TO USE BETWEEN <b>MAIN</b> AND <b>SECONDARY</b> COLOR THEMES</p>
    <div class="abs body-area"></div>
    <p class="abs graph-label" style="left:28px;top:77px"><b>Graph</b> Main Colors</p>
    <p class="abs graph-label" style="left:331px;top:77px"><b>Graph</b> Secondary Colors</p>

    <svg class="abs" style="left:24px;top:112px" width="256" height="190" viewBox="38 1020 256 190" font-family="Jost, Arial, sans-serif" font-size="8" fill="#3a3d42">
      <g stroke="#e3e3e3" stroke-width="1">
        <line x1="62" y1="1027" x2="280" y2="1027"/><line x1="62" y1="1069" x2="280" y2="1069"/>
        <line x1="62" y1="1111" x2="280" y2="1111"/><line x1="62" y1="1153" x2="280" y2="1153"/>
      </g>
      <text x="42" y="1030">100</text><text x="46" y="1072">75</text><text x="46" y="1114">50</text><text x="46" y="1156">25</text><text x="50" y="1197">0</text>
      <polygon points="62,1103 135,1122 205,1078 232,1082 278,1075 278,1195 62,1195" fill="var(--grey-series)"/>
      <polygon points="62,1145 135,1162 205,1150 278,1140 278,1195 62,1195" fill="var(--charcoal)"/>
      <polygon points="62,1165 135,1150 205,1105 278,1035 278,1195 62,1195" fill="var(--orange)"/>
      <line x1="62" y1="1195" x2="280" y2="1195" stroke="#3a3d42" stroke-width="1"/>
      <g font-weight="600"><text x="53" y="1205">2007</text><text x="125" y="1205">2008</text><text x="196" y="1205">2009</text><text x="268" y="1205">2010</text></g>
    </svg>

    <svg class="abs" style="left:319px;top:102px" width="200" height="200" viewBox="0 0 200 200" font-family="Jost, Arial, sans-serif" font-size="10" fill="#fff">
      <path d="M100 100 L62 187 A95 95 0 0 1 132.5 10.7 Z" fill="var(--blue)"/>
      <path d="M104.7 93.5 L137.2 4.2 A95 95 0 0 1 179.9 35.5 Z" fill="var(--green)"/>
      <path d="M100 100 L175.2 42 A95 95 0 0 1 192.6 121 Z" fill="var(--pink)"/>
      <path d="M100 100 L192.6 121 A95 95 0 0 1 62 187 Z" fill="var(--purple)"/>
      <text x="43" y="78">50%</text><text x="148" y="50">9%</text><text x="150" y="98">14%</text><text x="108" y="162">28%</text>
    </svg>
    <ul class="abs legend" style="left:516px;top:252px">
      <li><i style="background:var(--green)"></i>2007</li>
      <li><i style="background:var(--pink)"></i>2008</li>
      <li><i style="background:var(--purple)"></i>2009</li>
      <li><i style="background:var(--blue)"></i>2010</li>
    </ul>

    <ul class="abs note-list" style="left:38px;top:311px">
      <li><b>Aenean</b> ridiculus tortor quis interdum id habitant ad, natoque consectetuer nisl auctor libero quisque euismod ante inceptos malesuada ligula mattis.</li>
      <li>Varius inceptos <b>nascetur</b> mollis dui aptent ultrices. Pretium pulvinar ante lobortis convallis lectus netus vitae penatibus eros at blandit. Parturient.</li>
    </ul>
    <ul class="abs note-list" style="left:325px;top:311px">
      <li><b>Aenean</b> ridiculus tortor quis interdum id habitant ad, natoque consectetuer nisl auctor libero quisque euismod ante inceptos malesuada ligula mattis.</li>
      <li>Varius inceptos <b>nascetur</b> mollis dui aptent ultrices. Pretium pulvinar ante lobortis convallis lectus netus vitae penatibus eros at blandit. Parturient.</li>
    </ul>

    <footer class="abs footer">
      <div class="brand"><span class="brand-dot"></span><span class="brand-name">Harrowby &amp; Co.</span></div>
      <span class="divider"></span>
      <p class="deck">COMPANY PRESENTATION <span><em>to</em> Business<em>/client</em></span></p>
      <span class="page">8</span>
    </footer>
  </section>

  <!-- Back cover -->
  <section class="slide back" style="left:605px;top:908px">
    <div class="abs brand">
      <span class="brand-dot"></span>
      <div class="lockup">
        <span class="brand-name">Harrowby &amp; Co.</span>
        <p class="tagline">Accounting, Taxation &amp; Strategic Business Advisors</p>
      </div>
    </div>
    <div class="abs contact" style="top:343px">
      <h4>Contact us:</h4>
      <p>888-888-8888</p>
      <p>info@harrowbyco.com</p>
    </div>
    <div class="abs contact" style="top:388px">
      <h4>Central Office:</h4>
      <p>Address Line 1</p>
      <p>Address Line 2</p>
    </div>
    <p class="abs web">www.harrowbyco.com</p>
  </section>

</div>
</body>
</html>
```